Business Card for Bloom Vitality & Strength

Hi can you please design a business card with my logo and program logo (the new one I just sent) somewhere on it too maybe on the back? Needs to be eye catching and super cool.
Trudy Melcombe, Director
Master Personal Trainer & Nutrition Coach
0472 816 305
Www.bloomvitalitystrength.com.au
Insta (logo) bloom_vitality_strength #bloomyou7x72018

Target Market(s)

30+ women looking to change lifestyle to healthy mind body etc

Industry/Entity Type

Health And Wellness

Contact Information for Business Card

As above

Font styles to use
Sans Serif

Colors

Designer to choose colors to be used in the design.

Requirements
Must have
• Must super cool and edgy with a bit of cuteness

```html
<!DOCTYPE html>
<html lang="en">
<head>
<meta charset="utf-8">
<title>Bloom Vitality &amp; Strength – Business Card</title>
<link href="https://fonts.googleapis.com/css2?family=Lato:wght@400;700;900&display=swap" rel="stylesheet">
<style>
  :root {
    --backdrop: #3a3431;
    --card: #ffffff;
    --card-back: #efefef;
    --ink: #1a1a1a;
    --brand-red: #c8161d;
    --brand-black: #000000;
    --muted: #555555;
  }
  * { margin: 0; padding: 0; box-sizing: border-box; }
  html, body {
    width: 1200px; height: 844px; overflow: hidden;
    background: var(--backdrop);
    font-family: "Lato", sans-serif;
  }
  .card {
    position: absolute; top: 272px;
    width: 520px; height: 300px;
    box-shadow: 0 10px 28px rgba(0,0,0,.45);
  }
  .card--front { left: 60px; background: var(--card); }
  .card--back { left: 620px; background: var(--card-back); }

  .edge-stripe { position: absolute; left: 0; width: 12px; }
  .edge-stripe--red { top: 176px; height: 54px; background: var(--brand-red); }
  .edge-stripe--black { top: 230px; height: 50px; background: var(--brand-black); }

  .brand-name {
    position: absolute; top: 46px; right: 34px;
    display: flex; align-items: center; gap: 10px;
    font-weight: 900; font-size: 21px; color: var(--ink);
    text-transform: uppercase; letter-spacing: .5px;
  }
  .brand-dot { width: 26px; height: 26px; border-radius: 50%; background: var(--brand-red); }

  .person { position: absolute; left: 34px; top: 138px; color: var(--ink); }
  .person__name { font-weight: 700; font-size: 19px; color: var(--brand-red); text-transform: uppercase; }
  .person__role, .person__title { font-size: 14px; line-height: 1.35; }

  .contacts { position: absolute; left: 34px; top: 214px; list-style: none; font-size: 15px; color: var(--ink); }
  .contacts li { display: flex; align-items: center; gap: 7px; line-height: 1.45; }
  .contacts svg { width: 13px; height: 13px; flex: none; }
  .square-mark { width: 13px; height: 13px; background: var(--brand-red); border-radius: 2px; }

  .program {
    position: absolute; left: 0; right: 0; top: 96px;
    text-align: center; color: var(--ink);
  }
  .program__name { display: inline-flex; align-items: center; gap: 10px; font-size: 36px; font-weight: 400; letter-spacing: 2px; }
  .program__dot { width: 28px; height: 28px; border-radius: 50%; background: var(--brand-red); }
  .program__by { margin-top: 10px; font-size: 12px; color: var(--muted); }
</style>
</head>
<body>
  <section class="card card--front" aria-label="Business card front">
    <div class="edge-stripe edge-stripe--red"></div>
    <div class="edge-stripe edge-stripe--black"></div>

    <div class="brand-name"><span class="brand-dot"></span>Bloom Vitality &amp; Strength</div>

    <div class="person">
      <p class="person__name">Trudy Melcombe</p>
      <p class="person__role">Director</p>
      <p class="person__title">Master Personal Trainer &amp; Nutrition Coach</p>
    </div>

    <ul class="contacts">
      <li>
        <svg viewBox="0 0 24 24" aria-hidden="true"><path fill="#c8161d" d="M6.6 10.8a15 15 0 0 0 6.6 6.6l2.2-2.2a1 1 0 0 1 1-.25 11.4 11.4 0 0 0 3.6.57 1 1 0 0 1 1 1V20a1 1 0 0 1-1 1A17 17 0 0 1 3 4a1 1 0 0 1 1-1h3.5a1 1 0 0 1 1 1c0 1.25.2 2.45.57 3.57a1 1 0 0 1-.25 1z"/></svg>
        0472 816 305
      </li>
      <li>
        <svg viewBox="0 0 24 24" aria-hidden="true"><path fill="#c8161d" d="M12 2a7 7 0 0 0-7 7c0 5.2 7 13 7 13s7-7.8 7-13a7 7 0 0 0-7-7zm0 9.5A2.5 2.5 0 1 1 12 6.5a2.5 2.5 0 0 1 0 5z"/></svg>
        www.bloomvitalitystrength.com.au
      </li>
      <li><span class="square-mark"></span>bloom_vitality_strength #bloomyou7x72018</li>
    </ul>
  </section>

  <section class="card card--back" aria-label="Business card back">
    <div class="program">
      <div class="program__name"><span class="program__dot"></span>BloomYou7x7</div>
      <p class="program__by">By Bloom Vitality &amp; Strength</p>
    </div>
  </section>
</body>
</html>
```